Business Card Design Project

Kestrel Amber Ridge Farms, LLC is a small farm south of Fernhollow Oregon. The farm produces blueberries, cranberries, mushrooms and possible other crops in the future.
We plan on installing yurts on the property for rent and for a farm experience,

A clody/misty covered black moon should be the design. This could be the entire front of the card. (There is another pixel harbor project for this design). The back could be for the names, phone, address, etc.

Another option would be 3/4 of the card be the logo, then put the name, title, address, etc. vertically on the card right side front.

Target Market(s)

Customers of the farm, possible visitors using the yurts,

Industry/Entity Type

Farm

Other font styles liked:
• Hobo std

Colors

Designer to choose colors to be used in the design.

Requirements
Must have
• Consistent font usage

```html
<!DOCTYPE html>
<html lang="en">
<head>
<meta charset="utf-8">
<title>Kestrel Amber Ridge Farms – Business Card</title>
<link rel="stylesheet" href="https://fonts.googleapis.com/css2?family=Ubuntu:wght@700&family=Open+Sans:wght@400&display=swap">
<style>
  :root {
    --page: #e9e6e1;
    --card-dark: #050505;
    --card-mid: #2a2a2a;
    --ink: #f2f2f2;
    --ink-soft: #cfcfcf;
    --arc-line: #8a8a8a;
  }
  * { margin: 0; padding: 0; box-sizing: border-box; }
  html, body { width: 1200px; height: 1023px; overflow: hidden; }
  body {
    background: var(--page);
    display: flex;
    align-items: center;
    justify-content: center;
    gap: 80px;
    font-family: "Ubuntu", sans-serif;
  }
  .card {
    position: relative;
    width: 400px;
    height: 640px;
    border-radius: 4px;
    background: linear-gradient(160deg, var(--card-mid) 0%, var(--card-dark) 45%, #151515 100%);
    box-shadow: 0 14px 30px rgba(0,0,0,0.35);
    overflow: hidden;
    color: var(--ink);
  }
  .card-front .brand-name {
    position: absolute;
    top: 170px;
    left: 0;
    right: 0;
    text-align: center;
    font-weight: 700;
    font-size: 34px;
    line-height: 1.25;
    padding: 0 40px;
    color: var(--ink);
  }
  .card-front .location {
    position: absolute;
    top: 400px;
    left: 0;
    right: 0;
    text-align: center;
    font-weight: 700;
    font-size: 28px;
  }
  .card-back .arc {
    position: absolute;
    top: 0; left: 0;
    width: 400px;
    height: 200px;
  }
  .card-back .contact {
    position: absolute;
    top: 250px;
    left: 0; right: 0;
    text-align: center;
  }
  .person-name { font-weight: 700; font-size: 28px; }
  .person-title {
    font-family: "Open Sans", sans-serif;
    font-size: 12px;
    letter-spacing: 0.5px;
    color: var(--ink-soft);
    margin-top: 4px;
  }
  .details {
    font-family: "Open Sans", sans-serif;
    font-size: 13px;
    line-height: 1.45;
    margin-top: 34px;
  }
  .details .phone { margin-bottom: 18px; }
  .address {
    position: absolute;
    bottom: 70px;
    right: 36px;
    text-align: right;
    font-family: "Open Sans", sans-serif;
    font-style: normal;
    font-size: 13px;
    line-height: 1.5;
    letter-spacing: 0.5px;
    color: var(--ink-soft);
    text-transform: uppercase;
  }
</style>
</head>
<body>
  <section class="card card-front" aria-label="Card front">
    <h1 class="brand-name">Kestrel Amber Ridge Farms</h1>
    <p class="location">Fernhollow Oregon</p>
  </section>

  <section class="card card-back" aria-label="Card back">
    <svg class="arc" viewBox="0 0 400 200" aria-hidden="true">
      <defs>
        <linearGradient id="arcShade" x1="0" y1="0" x2="0" y2="1">
          <stop offset="0" stop-color="#000"/>
          <stop offset="1" stop-color="#1a1a1a"/>
        </linearGradient>
      </defs>
      <path d="M0 0 H400 V110 Q200 200 0 150 Z" fill="url(#arcShade)"/>
      <path d="M0 150 Q200 200 400 110" fill="none" stroke="var(--arc-line)" stroke-width="2" opacity="0.6"/>
    </svg>
    <div class="contact">
      <h2 class="person-name">Daniel Hartwell</h2>
      <p class="person-title">PRESIDENT</p>
      <div class="details">
        <p class="phone">541-555-0182</p>
        <p>daniel@kestrelamberridge.com</p>
        <p>www.kestrelamberridge.com</p>
      </div>
    </div>
    <address class="address">
      4120 Alder Hollow Lane<br>Fernhollow, Oregon 97499
    </address>
  </section>
</body>
</html>
```